Business Card for Industrial Distributor

We need a business card design for an industrial distributor. We sell machine parts for the manufacturing and oil industry. We would like the cards to look clean and modern but with a touch of industry.

Our colors are blue/white.

Please feel free to visit our website www.korvelindustrial.com

Target Market(s)

mexican manufacturers in the automobile/aerospace industry

Industry/Entity Type

Industrial

Colors
ffffff
0555a3

```html
<!DOCTYPE html>
<html lang="en">
<head>
<meta charset="utf-8">
<title>Korvel Business Card</title>
<link rel="stylesheet" href="https://fonts.googleapis.com/css2?family=Lato:wght@400;700;900&family=Arimo:wght@400&display=swap">
<style>
  :root {
    --brand-blue: #0555a3;
    --navy: #1b2a78;
    --card-blue-light: #2a4fb0;
    --card-blue-dark: #1a3589;
    --paper: #ffffff;
    --paper-shade: #eceef1;
    --ink: #2b2b2b;
    --stage: #2a2a2a;
  }
  * { margin: 0; padding: 0; box-sizing: border-box; }
  html, body { width: 1200px; height: 997px; overflow: hidden; }
  body {
    background: var(--stage);
    font-family: "Lato", sans-serif;
    position: relative;
  }
  .card {
    position: absolute;
    left: 250px;
    width: 700px;
    height: 400px;
    border-radius: 26px;
    overflow: hidden;
  }
  /* Back side */
  .card-back {
    top: 50px;
    background: linear-gradient(160deg, var(--card-blue-light), var(--card-blue-dark));
  }
  .back-logo {
    position: absolute;
    left: 0; right: 0; top: 160px;
    display: flex; align-items: center; justify-content: center; gap: 14px;
  }
  .back-logo .mark {
    width: 60px; height: 60px; border-radius: 50%;
    background: #d9dde6;
  }
  .back-logo .wordmark {
    font-weight: 900; font-size: 66px; color: #d9dde6; letter-spacing: 0.5px;
  }
  .tagline {
    position: absolute;
    left: 0; right: 0; bottom: 30px;
    text-align: center;
    color: var(--paper);
    font-size: 13px; font-weight: 700; letter-spacing: 1.4px;
    text-transform: uppercase;
  }
  /* Front side */
  .card-front {
    top: 510px;
    background: linear-gradient(160deg, var(--paper), var(--paper-shade));
  }
  .front-logo {
    position: absolute;
    right: 45px; top: 50px;
    display: flex; align-items: center; gap: 12px;
  }
  .front-logo .mark {
    width: 54px; height: 54px; border-radius: 50%;
    background: var(--brand-blue);
  }
  .front-logo .wordmark {
    font-weight: 900; font-size: 58px; color: var(--navy);
  }
  .divider {
    position: absolute;
    left: 250px; right: 45px; top: 196px;
    height: 2px; background: var(--navy);
  }
  .person {
    position: absolute; left: 45px; top: 170px;
  }
  .person .name {
    font-weight: 900; font-size: 24px; color: var(--navy);
  }
  .person .role {
    font-weight: 900; font-size: 13px; color: var(--ink); letter-spacing: 0.6px;
    text-transform: uppercase; margin-top: 2px;
  }
  .website {
    position: absolute; right: 45px; top: 216px;
    font-weight: 700; font-size: 17px; color: var(--navy);
  }
  .contacts {
    position: absolute; left: 45px; top: 236px;
    list-style: none;
    font-family: "Arimo", sans-serif; font-size: 17px; color: var(--ink);
  }
  .contacts li {
    display: flex; align-items: flex-start; gap: 12px; line-height: 24px; margin-bottom: 4px;
  }
  .contacts svg { flex: none; margin-top: 4px; }
</style>
</head>
<body>
  <section class="card card-back" aria-label="Card back">
    <div class="back-logo">
      <span class="mark"></span>
      <span class="wordmark">Korvel</span>
    </div>
    <p class="tagline">We sell machine parts for the manufacturing and oil industry.</p>
  </section>

  <section class="card card-front" aria-label="Card front">
    <div class="front-logo">
      <span class="mark"></span>
      <span class="wordmark">Korvel</span>
    </div>
    <div class="divider"></div>
    <div class="person">
      <p class="name">Dana Whitfield</p>
      <p class="role">Founder &amp; CEO</p>
    </div>
    <p class="website">www.korvelindustrial.com</p>
    <ul class="contacts">
      <li>
        <svg width="16" height="16" viewBox="0 0 16 16" aria-hidden="true"><circle cx="8" cy="8" r="8" fill="#1b2a78"/><path d="M5 4.5c0 3.5 2.5 6.5 6 7l1-1.5-1.8-1-0.8.8c-1-.5-2-1.5-2.5-2.5l.8-.8-1-1.8z" fill="#fff"/></svg>
        <span>(555) 214-3870</span>
      </li>
      <li>
        <svg width="16" height="16" viewBox="0 0 16 16" aria-hidden="true"><circle cx="8" cy="8" r="8" fill="#1b2a78"/><rect x="4.5" y="6" width="7" height="5" fill="#fff"/><rect x="6" y="4" width="4" height="2" fill="#fff"/></svg>
        <span>(555) 214-3874</span>
      </li>
      <li>
        <svg width="16" height="16" viewBox="0 0 16 16" aria-hidden="true"><circle cx="8" cy="8" r="8" fill="#1b2a78"/><rect x="4" y="5.5" width="8" height="5.5" fill="#fff"/><path d="M4 5.5l4 3 4-3" stroke="#1b2a78" fill="none"/></svg>
        <span>sales@korvelindustrial.com</span>
      </li>
      <li>
        <svg width="16" height="16" viewBox="0 0 16 16" aria-hidden="true"><circle cx="8" cy="8" r="8" fill="#1b2a78"/><path d="M8 3.8l4 3.5h-1.2v4.2H5.2V7.3H4z" fill="#fff"/></svg>
        <span>4820 Foundry Line Rd,<br>Riverton, TX 78000</span>
      </li>
    </ul>
  </section>
</body>
</html>
```